Velisto Events Business Card

We need a business cards that stands out to our clients. We are company who targets prestige clients to spend money with us on experiences, so our image needs to be prestige
Target Market(s)
Corporate
Contact Information for Business Card
There will be four different names on the business cards
Dana Morrowby
Director
O: 02 5147 3086
M: 0451 692 038
E: info@velistoevents.example.au
Facebook: @velistoevents
Instagram: velistoevents
www.velistoevents.example.au
Nathaniel Morrowby
Director
O: 02 5147 3086
M: 0467 215 904
Facebook: @velistoevents
Instagram: velistoevents
www.velistoevents.example.au
Teodor Vinkel
Director
O: 02 5147 3086
M: 0478 903 527
Facebook: @velistoevents
Instagram: velistoevents
www.velistoevents.example.au
Mabel Hartung
Director
O: 02 5147 3086
Facebook: @velistoevents
Instagram: velistoevents
www.velistoevents.example.au
Colors
Designer to choose colors to be used in the design.
Look and feel

```html
<!DOCTYPE html>
<html lang="en">
<head>
<meta charset="utf-8">
<title>Velisto Events Business Card</title>
<link rel="stylesheet" href="https://fonts.googleapis.com/css2?family=Cinzel:wght@500&family=Open+Sans:wght@400;600&display=swap">
<style>
  :root {
    --stage-top: #2c2d57;
    --stage-bottom: #1c1b44;
    --navy: #201e52;
    --navy-deep: #1c1a4a;
    --gold: #d8a844;
    --gold-light: #fbe7a6;
    --gold-deep: #f3a51e;
    --paper: #ffffff;
    --paper-shade: #ececef;
    --ink: #2a2a4a;
    --white: #ffffff;
  }
  * { margin: 0; padding: 0; box-sizing: border-box; }
  html, body { width: 1200px; height: 1200px; overflow: hidden; }
  body {
    position: relative;
    background: linear-gradient(160deg, var(--stage-top), var(--stage-bottom));
    font-family: "Open Sans", Arial, sans-serif;
  }
  .card {
    position: absolute;
    left: 324px;
    width: 601px;
    height: 373px;
    border-radius: 3px;
    overflow: hidden;
    box-shadow: 0 12px 40px rgba(0, 0, 0, 0.45);
  }
  .card-front {
    top: 172px;
    background: linear-gradient(90deg, var(--navy), var(--navy-deep));
  }
  .card-back {
    top: 643px;
    background: linear-gradient(90deg, var(--paper-shade), var(--paper) 70%);
  }
  .brand {
    position: absolute;
    left: 0; right: 0;
    text-align: center;
    font-family: "Cinzel", Georgia, serif;
    font-weight: 500;
    color: var(--gold);
  }
  .brand-mark {
    display: block;
    margin: 0 auto;
    background: var(--gold);
  }
  .brand-name { display: block; }
  .brand-sub { display: block; }

  .card-front .brand { top: 300px; }
  .card-front .brand-mark { width: 40px; height: 40px; margin-bottom: 40px; margin-top: -220px; }
  .card-front .brand { top: 310px; }
  .card-front .brand-name { font-size: 36px; letter-spacing: 6px; line-height: 1; }
  .card-front .brand-sub { font-size: 17px; letter-spacing: 6px; margin-top: 10px; }

  .front-bar {
    position: absolute;
    left: 66px;
    bottom: 0;
    width: 470px;
    height: 12px;
    border-radius: 8px 8px 0 0;
    background: linear-gradient(90deg, var(--gold-deep), var(--gold-light) 40%, #c99a2e 70%, var(--gold-light));
  }

  .back-band {
    position: absolute;
    left: 209px;
    top: 0;
    width: 171px;
    height: 227px;
    background: var(--navy);
  }
  .card-back .brand { top: 42px; }
  .card-back .brand-mark { width: 28px; height: 28px; margin-bottom: 22px; }
  .card-back .brand-name { font-size: 20px; letter-spacing: 3px; line-height: 1; }
  .card-back .brand-sub { font-size: 11px; letter-spacing: 3px; margin-top: 5px; }

  .person {
    position: absolute;
    top: 164px;
    left: 0; right: 0;
    text-align: center;
    color: var(--white);
    font-size: 14px;
    line-height: 18px;
  }
  .person-role { font-weight: 600; font-size: 15px; }

  .back-rule {
    position: absolute;
    left: 41px;
    top: 228px;
    width: 516px;
    height: 2px;
    background: linear-gradient(90deg, transparent, var(--gold) 20%, var(--gold-light) 60%, transparent);
  }
  .contact {
    position: absolute;
    top: 249px;
    left: 0;
    width: 597px;
    text-align: center;
    color: var(--ink);
    font-size: 10.5px;
    line-height: 14.5px;
  }

  .ornament {
    position: absolute;
    left: 88px;
    top: 1065px;
    width: 124px;
    height: 120px;
    border-radius: 50%;
    background: radial-gradient(circle, rgba(243, 165, 30, 0.55), rgba(243, 165, 30, 0.08) 70%);
  }
  .stage-rule {
    position: absolute;
    left: 205px;
    top: 1124px;
    width: 937px;
    height: 3px;
    background: linear-gradient(90deg, var(--gold-deep), var(--gold-light) 60%, var(--gold));
    clip-path: polygon(0 0, 100% 50%, 0 100%);
  }
</style>
</head>
<body>
  <section class="card card-front" aria-label="Card front">
    <div class="brand">
      <span class="brand-mark"></span>
      <span class="brand-name">VELISTO</span>
      <span class="brand-sub">EVENTS</span>
    </div>
    <div class="front-bar"></div>
  </section>

  <section class="card card-back" aria-label="Card back">
    <div class="back-band">
      <div class="brand">
        <span class="brand-mark"></span>
        <span class="brand-name">VELISTO</span>
        <span class="brand-sub">EVENTS</span>
      </div>
      <div class="person">
        <p class="person-name">Dana Morrowby</p>
        <p class="person-role">Director</p>
        <p class="person-phone">M: 0451 692 038</p>
      </div>
    </div>
    <div class="back-rule"></div>
    <div class="contact">
      <p>E: info@velistoevents.example.au</p>
      <p>Facebook: @velistoevents</p>
      <p>Instagram: velistoevents</p>
      <p>www.velistoevents.example.au</p>
    </div>
  </section>

  <div class="ornament" role="img" aria-label="Gold filigree flourish ornament"></div>
  <div class="stage-rule"></div>
</body>
</html>
```